Business card required for IT Consultancy Business - Bluefern Consulting.
Company provides the whole nine yards of services across IT Architecture, design and execution.
Basically we provide consulting services to help businesses make sure their technology is enabling their business strategy.
Design for front and back required.
We would like the front of the card to inlcude:
Name
Title
Mobile number
email address
www.BFQ.com.au
Company logos attached.
Thank you
Industry/Entity Type
Business
Contact Information for Business Card
Name
Title
Mobile number
email address
www.BFQ.com.au
Look and feel
Each slider illustrates characteristics of the customer's brand and the style your logo design should communicate.

```html
<!DOCTYPE html>
<html lang="en">
<head>
<meta charset="utf-8">
<title>Bluefern Consulting – Business Card</title>
<link rel="stylesheet" href="https://fonts.googleapis.com/css2?family=Open+Sans:wght@400;600;700&display=swap">
<style>
  :root {
    --brand-blue: #0f6db8;
    --brand-orange: #e8602c;
    --ink-grey: #555b61;
    --card-white: #f7f7f5;
    --backdrop: #2a2a2c;
    --wash-orange: rgba(232, 96, 44, 0.10);
  }
  * { box-sizing: border-box; margin: 0; padding: 0; }
  html, body {
    width: 1200px; height: 900px; overflow: hidden;
    background: var(--backdrop);
    font-family: "Open Sans", Arial, sans-serif;
  }
  .stage { position: relative; width: 1200px; height: 900px; }
  .card {
    position: absolute;
    width: 600px; height: 343px;
    box-shadow: 0 10px 28px rgba(0,0,0,0.45);
    overflow: hidden;
  }
  .card--back {
    left: 110px; top: 100px;
    background: var(--brand-blue);
    color: #fff;
  }
  .card--front {
    left: 490px; top: 460px;
    background: var(--card-white);
  }
  .wordmark {
    display: flex; align-items: center; gap: 12px;
    font-weight: 700; line-height: 1;
  }
  .wordmark__dot {
    width: 18px; height: 18px; border-radius: 50%;
    background: currentColor; flex: none;
  }
  .card--back .wordmark {
    position: absolute; left: 0; right: 0; top: 130px;
    justify-content: center;
    font-size: 40px; color: #fff;
  }
  .back-url {
    position: absolute; left: 0; right: 0; top: 255px;
    text-align: center; font-size: 13px; letter-spacing: 6px;
    color: rgba(255,255,255,0.9);
  }
  .card--front .wordmark {
    position: absolute; right: 40px; top: 52px;
    font-size: 30px; color: var(--brand-blue);
  }
  .front-wash {
    position: absolute; left: 40px; top: 110px;
    width: 260px; height: 260px; border-radius: 50%;
    background: var(--wash-orange);
  }
  .front-rule {
    position: absolute; left: 40px; right: 40px; top: 150px;
    height: 1px; background: var(--brand-blue); opacity: 0.7;
  }
  .contact {
    position: absolute; left: 40px; bottom: 36px;
    font-size: 14px; color: var(--ink-grey);
  }
  .contact__name {
    font-weight: 700; color: var(--brand-blue);
    text-transform: uppercase; font-size: 15px; margin-bottom: 6px;
  }
  .contact__title { color: var(--brand-orange); font-weight: 600; }
  .contact__line span { margin-right: 14px; }
  .contact__label { font-weight: 700; color: var(--brand-blue); margin-right: 4px !important; }
</style>
</head>
<body>
<main class="stage">
  <section class="card card--back" aria-label="Card back">
    <div class="wordmark"><span class="wordmark__dot"></span>Bluefern Consulting</div>
    <p class="back-url">www.BFQ.com.au</p>
  </section>

  <section class="card card--front" aria-label="Card front">
    <div class="front-wash"></div>
    <div class="wordmark"><span class="wordmark__dot"></span>Bluefern Consulting</div>
    <div class="front-rule"></div>
    <div class="contact">
      <p class="contact__name">Alex Morgan <span class="contact__title">- CEO/FOUNDER</span></p>
      <p class="contact__line">
        <span class="contact__label">M :</span><span>555 010 2471</span>
        <span class="contact__label">E :</span><span>alex@bfq.com.au</span>
        <span class="contact__label">W :</span><span>www.BFQ.com.au</span>
      </p>
    </div>
  </section>
</main>
</body>
</html>
```